依頼詳細
店名の看板は既に出来ておりますので、そちらの字体を参考にお願いします。
夫婦で営む小さなお店になります。
夫婦共に猫が大好きですので、夫婦をイメージした2匹の猫をどこかにデザインしていただきたいです。
記載項目
黒地の紙 店名はシルバー系希望 他はお任せいたします。
表面:店名、住所、電話番号、20時OPEN、月曜店休
裏面:簡単なマップ、インスタQRコード
希望イメージ
シンプル 複雑
単色 カラフル
暗い 明るい
日常 高級
遊び心 厳粛
未来的 伝統的
女性的 男性的
希望する色
無彩色系
納品ファイル
• 高解像度JPG (.jpg)
• イラストレーター形式 (.ai)
• フォトショップ形式 (.psd)
• PNG形式 (.png)
補足説明
■ 選んだ理由

寄り添う二匹の猫のシルエットが素敵でした。

■ 提案者全員のお礼・コメント

コンペに参加していただいた皆様、ありがとうございました。
皆様とても素晴らしい作品でした。
また機会がございましたら宜しくお願い致します。

```html
<!DOCTYPE html>
<html lang="ja">
<head>
<meta charset="utf-8">
<title>BAR HAVEN</title>
<link href="https://fonts.googleapis.com/css2?family=Roboto:wght@900&family=Playball&family=Noto+Sans+JP:wght@400&display=swap" rel="stylesheet">
<style>
  :root {
    --ground-dark: #1f1e1d;
    --ground-mid: #3b3937;
    --silhouette: #0b0b0b;
    --silhouette-edge: #2a2a2a;
    --silver: #c9c9c9;
    --text-white: #f2f2f2;
  }
  html, body {
    margin: 0;
    padding: 0;
    overflow: hidden;
    background: var(--ground-dark);
  }
  .card {
    position: relative;
    width: 726px;
    height: 1200px;
    overflow: hidden;
    background: radial-gradient(ellipse at 50% 45%, var(--ground-mid) 0%, #302e2c 55%, var(--ground-dark) 100%);
    font-family: "Noto Sans JP", sans-serif;
    color: var(--text-white);
  }
  .cat-pair {
    position: absolute;
    left: 182px;
    top: 254px;
    width: 362px;
    height: 400px;
  }
  .shop-name {
    position: absolute;
    left: 0;
    width: 100%;
    top: 672px;
    margin: 0;
    text-align: center;
    font-family: "Roboto", sans-serif;
    font-weight: 900;
    font-size: 60px;
    letter-spacing: 2px;
    color: var(--silver);
  }
  .opening {
    position: absolute;
    left: 0;
    width: 100%;
    top: 808px;
    margin: 0;
    text-align: center;
    font-family: "Playball", cursive;
    font-size: 56px;
    color: var(--text-white);
  }
  .closed-day {
    position: absolute;
    left: 0;
    width: 100%;
    top: 898px;
    margin: 0;
    text-align: center;
    font-size: 22px;
  }
  .contact {
    position: absolute;
    left: 280px;
    top: 1082px;
    margin: 0;
    display: grid;
    grid-template-columns: 130px auto;
    row-gap: 4px;
    align-items: baseline;
  }
  .contact dt {
    font-family: "Playball", cursive;
    font-size: 36px;
    text-align: right;
    padding-right: 12px;
    line-height: 40px;
  }
  .contact dd {
    margin: 0;
    font-size: 20px;
  }
</style>
</head>
<body>
  <main class="card">
    <svg class="cat-pair" viewBox="0 0 362 400" role="img" aria-label="Illustration of two black cat silhouettes sitting face to face with tails joined">
      <defs>
        <radialGradient id="cat-fill" cx="50%" cy="55%" r="60%">
          <stop offset="0%" stop-color="var(--silhouette)"/>
          <stop offset="100%" stop-color="var(--silhouette-edge)"/>
        </radialGradient>
      </defs>
      <rect width="362" height="400" rx="24" fill="url(#cat-fill)"/>
    </svg>

    <h1 class="shop-name">BAR HAVEN</h1>

    <p class="opening">Open:20:00~</p>
    <p class="closed-day">定休日:月曜日</p>

    <dl class="contact">
      <dt>Address</dt>
      <dd>東京都港区青葉坂00-00-00</dd>
      <dt>Tel</dt>
      <dd>0120-111-222</dd>
    </dl>
  </main>
</body>
</html>
```